Book Cover Font/Typesetting on Provided Cover Artwork - Family Memoir

I have the artwork for the book cover, but need the title, subtitle, and author's name designed against it. I have uploaded the cover artwork.

The title of the book: Finding Moira The subtitle of the book: One Winter's Promise The author's name: Dale Honcutt That's all of the text for the front cover. Thanks.

```html
<!DOCTYPE html>
<html lang="en">
<head>
<meta charset="utf-8">
<title>Finding Moira — Dale Honcutt</title>
<link rel="stylesheet" href="https://fonts.googleapis.com/css2?family=Yeseva+One&family=Playfair+Display:wght@700;800&display=swap">
<style>
  :root {
    --rust: #c94f26;
    --cream: #f3dfae;
    --umber: #5a4a3e;
    --rule: #6b5e54;
    --art-light: #ece8df;
    --art-mist: #d6dcd8;
    --art-moss: #8c8a6a;
    --art-earth: #5f5a40;
  }
  * { margin: 0; padding: 0; box-sizing: border-box; }
  html, body { width: 857px; height: 1200px; overflow: hidden; background: #fff; }
  .cover { position: relative; width: 857px; height: 1200px; overflow: hidden; }

  .cover-art {
    position: absolute; inset: 0;
    background:
      radial-gradient(ellipse 300px 200px at 720px 520px, rgba(240,236,170,0.55), transparent 70%),
      radial-gradient(ellipse 380px 420px at 170px 680px, rgba(200,205,210,0.6), transparent 70%),
      linear-gradient(180deg, var(--art-light) 0%, var(--art-mist) 45%, #dcd9cc 70%, var(--art-moss) 88%, var(--art-earth) 100%);
  }

  .band { position: absolute; left: 0; width: 100%; background: var(--rust); }
  .band-top { top: 0; height: 68px; display: flex; align-items: center; justify-content: center; }
  .band-bottom { bottom: 0; height: 20px; }

  .author {
    font-family: "Playfair Display", serif; font-weight: 700;
    font-size: 21px; letter-spacing: 0.62em; color: var(--cream);
    text-transform: uppercase; padding-left: 0.62em;
  }

  .title {
    position: absolute; left: 0; top: 0;
    font-family: "Yeseva One", serif; color: var(--rust); font-weight: 400;
  }
  .title-line { position: absolute; white-space: nowrap; font-size: 150px; line-height: 1; }
  .title-line.first { left: 114px; top: 175px; }
  .title-line.second { left: 290px; top: 318px; }

  .subtitle {
    position: absolute; left: 459px; top: 668px; width: 262px;
    text-align: center; font-family: "Playfair Display", serif; font-weight: 800;
    color: var(--umber); text-transform: uppercase;
  }
  .subtitle-lead { display: flex; align-items: center; gap: 10px; font-size: 40px; line-height: 1; }
  .subtitle-lead::before, .subtitle-lead::after { content: ""; flex: 1; height: 2px; background: var(--rule); }
  .subtitle-line { display: block; font-size: 42px; line-height: 1.3; letter-spacing: -0.01em; }
  .subtitle-rule { margin-top: 18px; height: 2px; background: var(--rule); }

  .frame-line { position: absolute; left: 821px; top: 184px; width: 2px; height: 880px; background: rgba(90,90,90,0.55); }
  .frame-line.inner { left: 800px; top: 184px; height: 40px; }

  .rings { position: absolute; left: 360px; top: 950px; }
</style>
</head>
<body>
<main class="cover">
  <div class="cover-art" role="img" aria-label="Painted collage artwork with a vintage photograph of a small child standing before a misty, textured landscape"></div>

  <header class="band band-top"><p class="author">Dale Honcutt</p></header>

  <h1 class="title">
    <span class="title-line first">Finding</span>
    <span class="title-line second">Moira</span>
  </h1>

  <div class="frame-line"></div>

  <p class="subtitle">
    <span class="subtitle-lead">One</span>
    <span class="subtitle-line">Winter's</span>
    <span class="subtitle-line">Promise</span>
    <span class="subtitle-rule" style="display:block"></span>
  </p>

  <svg class="rings" width="260" height="240" viewBox="0 0 260 240" aria-hidden="true">
    <g fill="none" stroke="#7a7570" stroke-width="1.2" opacity="0.7">
      <circle cx="190" cy="55" r="52"/>
      <circle cx="145" cy="110" r="60"/>
      <circle cx="75" cy="190" r="68"/>
    </g>
  </svg>

  <div class="band band-bottom"></div>
</main>
</body>
</html>
```